Medical VIP club - small design

Please read the specs in a design brief attached. Also we don't have logo in a Vector format and attaching the only version we have.

Industry/Entity Type

Club

```html
<!DOCTYPE html>
<html lang="en">
<head>
<meta charset="utf-8">
<title>Veridane — Medical VIP Club</title>
<link rel="stylesheet" href="https://fonts.googleapis.com/css2?family=Exo+2:wght@300;400;600;700&family=Arimo:wght@400&display=swap">
<style>
  :root {
    --bar-dark: #1e1605;
    --page-brown: #6a5841;
    --band-brown: #3b2f16;
    --cream: #f0ead8;
    --cream-light: #f6f3e6;
    --cream-mid: #e4dec6;
    --ink: #2a2010;
    --tile-dark: #201605;
    --panel: rgba(28, 19, 4, 0.78);
    --footer-mark: #4e4128;
    --icon-grey: #8f8f84;
  }
  * { margin: 0; padding: 0; box-sizing: border-box; }
  html, body { width: 1200px; height: 950px; overflow: hidden; }
  body {
    position: relative;
    background: var(--page-brown);
    font-family: "Exo 2", sans-serif;
    color: var(--cream);
  }
  .top-bar { position: absolute; left: 0; top: 0; width: 1200px; height: 17px; background: var(--bar-dark); }
  .hero-band { position: absolute; left: 0; top: 188px; width: 1200px; height: 367px; background: var(--band-brown); }

  .brand { position: absolute; left: 146px; top: 52px; display: flex; align-items: center; gap: 10px; }
  .brand-dot { width: 30px; height: 30px; border-radius: 50%; background: var(--cream); }
  .brand-name { font-size: 36px; font-weight: 600; color: var(--cream); letter-spacing: 0.5px; line-height: 1; white-space: nowrap; }

  .phone { position: absolute; right: 140px; top: 60px; font-size: 29px; font-weight: 300; color: var(--cream); letter-spacing: 0.5px; white-space: nowrap; }

  .main-nav { position: absolute; left: 114px; top: 128px; width: 960px; height: 53px; }
  .main-nav svg { position: absolute; left: 0; top: 0; }
  .nav-list { position: absolute; left: 0; top: 0; height: 53px; list-style: none; width: 960px; }
  .nav-item { position: absolute; top: 0; height: 53px; line-height: 55px; font-size: 18.5px; font-weight: 600; color: var(--ink); text-align: center; white-space: nowrap; letter-spacing: -0.2px; }
  .nav-item.is-active { color: var(--cream); }

  .slider { position: absolute; left: 114px; top: 181px; width: 960px; height: 392px; background: var(--cream-mid); box-shadow: 0 3px 6px rgba(0,0,0,0.25); }
  .slide-photo { position: absolute; left: 8px; top: 0; width: 944px; height: 384px;
    background: linear-gradient(90deg, #8a5a1c 0%, #b8271a 6%, #6a3d12 22%, #2a1a08 36%, #c69a4a 50%, #2a1a08 62%, #7a4a18 76%, #b32a18 92%, #8a5a1c 100%); }
  .slide-caption { position: absolute; left: 593px; top: 0; width: 289px; height: 208px; background: var(--panel); }
  .slide-title { position: absolute; left: 11px; top: 56px; font-size: 55px; font-weight: 700; line-height: 1; color: var(--cream); white-space: nowrap; letter-spacing: -0.5px; }
  .slide-text { position: absolute; left: 14px; top: 120px; font-size: 20px; font-weight: 400; line-height: 25px; color: var(--cream); white-space: nowrap; }
  .slide-next { position: absolute; left: 232px; top: 126px; }
  .slider-arrow { position: absolute; top: 175px; width: 50px; height: 50px; border-radius: 50%; background: var(--cream-light); }
  .slider-arrow svg { position: absolute; left: 17px; top: 13px; }
  .slider-arrow.prev { left: -13px; }
  .slider-arrow.next { left: 927px; }

  .service-tiles { position: absolute; left: 122px; top: 613px; }
  .tile { position: absolute; top: 0; width: 180px; height: 180px; background: var(--tile-dark); border-radius: 3px; overflow: hidden; }
  .tile-title { height: 37px; line-height: 37px; text-align: center; font-size: 15.5px; font-weight: 600; letter-spacing: -0.5px; white-space: nowrap; color: var(--cream); }
  .tile-photo { width: 180px; height: 134px; }
  .tile-photo.emergency { background: linear-gradient(160deg, #f4ecd8 0%, #7a7468 55%, #2c2820 100%); }
  .tile-photo.transport { background: linear-gradient(160deg, #8a7e6a 0%, #3a342a 60%, #0e0c08 100%); }
  .tile-photo.hotel { background: linear-gradient(180deg, #5a1a10 0%, #c89a68 45%, #8a3a20 100%); }
  .tile-photo.medical { background: linear-gradient(160deg, #4a6a30 0%, #6a9a48 50%, #2e4420 100%); }
  .tile-photo.member { background: linear-gradient(110deg, #f2ead8 0%, #d8c8a8 50%, #7a2018 100%); }

  .site-footer { position: absolute; left: 0; top: 831px; width: 1200px; height: 119px; background: var(--bar-dark); }
  .footer-brand { position: absolute; left: 160px; top: 34px; display: flex; align-items: center; gap: 8px; }
  .footer-brand .brand-dot { width: 22px; height: 22px; background: var(--footer-mark); }
  .footer-brand .brand-name { font-size: 27px; color: var(--footer-mark); }
  .copyright { position: absolute; left: 333px; top: 27px; font-family: "Arimo", sans-serif; font-size: 12px; color: #ffffff; white-space: nowrap; }
  .social { position: absolute; left: 973px; top: 21px; display: flex; gap: 8px; }
  .social-link { width: 25px; height: 25px; border-radius: 3px; background: linear-gradient(180deg, #b0b0a6, var(--icon-grey)); }
</style>
</head>
<body>
  <div class="top-bar"></div>
  <div class="hero-band"></div>

  <header>
    <div class="brand"><span class="brand-dot"></span><span class="brand-name">veridane</span></div>
    <div class="phone">212-555-0147</div>

    <nav class="main-nav">
      <svg width="960" height="53" viewBox="0 0 960 53" aria-hidden="true">
        <defs>
          <linearGradient id="navFill" x1="0" y1="0" x2="0" y2="1">
            <stop offset="0" stop-color="#f7f4e8"/>
            <stop offset="1" stop-color="#e2dcc4"/>
          </linearGradient>
        </defs>
        <path d="M30 0 H960 V53 H0 V42 Z" fill="url(#navFill)"/>
        <g stroke="#d2ccb4" stroke-width="1">
          <line x1="142.5" y1="0" x2="142.5" y2="53"/>
          <line x1="260.5" y1="0" x2="260.5" y2="53"/>
          <line x1="373.5" y1="0" x2="373.5" y2="53"/>
          <line x1="481.5" y1="0" x2="481.5" y2="53"/>
          <line x1="950.5" y1="0" x2="950.5" y2="53"/>
        </g>
        <path d="M704 4 H837 V53 H696 V12 Z" fill="#1e1605"/>
      </svg>
      <ul class="nav-list">
        <li class="nav-item" style="left:60px;width:76px">Home</li>
        <li class="nav-item" style="left:143px;width:117px">About Us</li>
        <li class="nav-item" style="left:261px;width:112px">VIP Club</li>
        <li class="nav-item" style="left:374px;width:107px">Services</li>
        <li class="nav-item" style="left:482px;width:214px">Packages and Prices</li>
        <li class="nav-item is-active" style="left:696px;width:141px">Registration</li>
        <li class="nav-item" style="left:837px;width:113px">Contacts</li>
      </ul>
    </nav>
  </header>

  <main>
    <section class="slider">
      <div class="slide-photo" role="img" aria-label="Luxurious hotel corridor with red glass panels, gold frames and a checkered marble floor"></div>
      <div class="slide-caption">
        <h1 class="slide-title">VIP Club</h1>
        <p class="slide-text">Reserve Your<br>Membership Today</p>
        <svg class="slide-next" width="26" height="42" viewBox="0 0 26 42" aria-hidden="true">
          <path d="M4 2 L22 21 L4 40" fill="none" stroke="#f0ead8" stroke-width="7"/>
        </svg>
      </div>
      <div class="slider-arrow prev">
        <svg width="16" height="24" viewBox="0 0 16 24" aria-hidden="true"><path d="M13 2 L4 12 L13 22" fill="none" stroke="#1e1605" stroke-width="5"/></svg>
      </div>
      <div class="slider-arrow next">
        <svg width="16" height="24" viewBox="0 0 16 24" aria-hidden="true"><path d="M3 2 L12 12 L3 22" fill="none" stroke="#1e1605" stroke-width="5"/></svg>
      </div>
    </section>

    <section class="service-tiles">
      <article class="tile" style="left:0">
        <h2 class="tile-title">Emergency Services</h2>
        <div class="tile-photo emergency" role="img" aria-label="Ambulance with lights on at night"></div>
      </article>
      <article class="tile" style="left:190px">
        <h2 class="tile-title">Transportation Services</h2>
        <div class="tile-photo transport" role="img" aria-label="Private jet cabin with leather seats"></div>
      </article>
      <article class="tile" style="left:380px">
        <h2 class="tile-title">Hotel Services</h2>
        <div class="tile-photo hotel" role="img" aria-label="Grand hotel entrance with red carpet"></div>
      </article>
      <article class="tile" style="left:570px">
        <h2 class="tile-title">Medical Professionals</h2>
        <div class="tile-photo medical" role="img" aria-label="Doctor in green scrubs with crossed arms"></div>
      </article>
      <article class="tile" style="left:760px">
        <h2 class="tile-title">Become a Member</h2>
        <div class="tile-photo member" role="img" aria-label="Marble staircase with a red velvet rope"></div>
      </article>
    </section>
  </main>

  <footer class="site-footer">
    <div class="footer-brand"><span class="brand-dot"></span><span class="brand-name">veridane</span></div>
    <p class="copyright">Copyright 2010 Veridane. All rights reserved.</p>
    <div class="social">
      <span class="social-link" aria-label="News feed"></span>
      <span class="social-link" aria-label="Social network"></span>
      <span class="social-link" aria-label="Social network"></span>
    </div>
  </footer>
</body>
</html>
```